MORVANE GROUP (STATIONARY)
MORVANE CONSULTING GROUP, LLC
Please update design to show my name next to the Title, Principal : Delbert T. Worrow III
Also, please fix the address in the design :
4827 Halvorsen St. NW, Washington, DC 20374
Last, I am also looking for other stationary such as letterhead , letters and invoices. (not just the business card)
Thank you!
Delbert

```html
<!DOCTYPE html>
<html lang="en">
<head>
<meta charset="utf-8">
<title>Morvane Group – Business Card</title>
<link rel="stylesheet" href="https://fonts.googleapis.com/css2?family=Arimo:wght@400;700&display=swap">
<style>
  :root {
    --backdrop: #e9e6e2;
    --card: #ffffff;
    --band-dark: #4a4a4c;
    --band-light: #c9c9cb;
    --ink: #3b3b3d;
    --ink-soft: #8a8a8c;
    --rule: #9a9a9c;
    --mark: #5e5e60;
  }
  * { margin: 0; padding: 0; box-sizing: border-box; }
  html, body {
    width: 1200px; height: 780px; overflow: hidden;
    background: var(--backdrop);
    font-family: "Arimo", Arial, sans-serif;
    color: var(--ink);
  }
  .card {
    position: absolute; left: 75px; top: 90px;
    width: 1050px; height: 600px;
    border-radius: 44px;
    background: var(--card);
    overflow: hidden;
    box-shadow: 0 10px 30px rgba(0,0,0,0.12);
  }
  .card-bands { position: absolute; inset: 0; width: 100%; height: 100%; }
  .brand {
    position: absolute; left: 190px; top: 120px;
    display: flex; align-items: center; gap: 30px;
  }
  .brand-mark {
    width: 120px; height: 120px; border-radius: 50%;
    background: var(--mark);
  }
  .brand-name {
    font-weight: 400; font-size: 92px; letter-spacing: 6px;
    color: var(--ink); line-height: 1; text-transform: uppercase;
  }
  .brand-name small {
    display: block; text-align: right;
    font-size: 46px; letter-spacing: 5px; margin-top: 8px;
  }
  .divider {
    position: absolute; left: 470px; top: 335px;
    width: 2px; height: 195px; background: var(--rule);
  }
  .holder {
    position: absolute; right: 610px; top: 418px; text-align: right;
    white-space: nowrap;
  }
  .holder-name { font-weight: 700; font-size: 27px; color: var(--ink); }
  .holder-title { font-size: 22px; color: var(--ink-soft); margin-top: 4px; }
  .contact {
    position: absolute; left: 500px; top: 338px;
    font-size: 23px; line-height: 1.3; color: var(--ink);
    white-space: nowrap;
  }
  .contact-address { margin-bottom: 24px; }
  .contact-line { display: flex; align-items: center; gap: 12px; margin-top: 8px; }
  .contact-line svg { width: 20px; height: 20px; flex: none; }
</style>
</head>
<body>
  <div class="card">
    <svg class="card-bands" viewBox="0 0 1050 600" aria-hidden="true">
      <path d="M0 0 H140 C80 120 60 300 100 600 H0 Z" fill="var(--band-light)"/>
      <path d="M0 0 H105 C52 130 38 300 72 600 H0 Z" fill="var(--band-dark)"/>
      <path d="M1050 600 H920 C985 480 1000 300 965 0 H1050 Z" fill="var(--band-light)"/>
      <path d="M1050 600 H955 C1008 470 1020 300 992 0 H1050 Z" fill="var(--band-dark)"/>
    </svg>

    <div class="brand">
      <div class="brand-mark"></div>
      <div class="brand-name">Morvane<small>Group</small></div>
    </div>

    <div class="holder">
      <div class="holder-name">Delbert T. Worrow III</div>
      <div class="holder-title">Principal</div>
    </div>

    <div class="divider"></div>

    <div class="contact">
      <div class="contact-address">4827 Halvorsen St. NW<br>Washington, DC 20374</div>
      <div class="contact-line">
        <svg viewBox="0 0 24 24"><rect x="6" y="1" width="12" height="22" rx="2" fill="var(--ink)"/><rect x="8" y="4" width="8" height="12" fill="#fff"/><circle cx="12" cy="19.5" r="1.4" fill="#fff"/></svg>
        <span>202-555-0187</span>
      </div>
      <div class="contact-line">
        <svg viewBox="0 0 24 24"><circle cx="12" cy="12" r="4" fill="none" stroke="var(--ink)" stroke-width="2.4"/><path d="M16 8v5.5a2.5 2.5 0 0 0 5 0V12a9 9 0 1 0-3.5 7.1" fill="none" stroke="var(--ink)" stroke-width="2.4"/></svg>
        <span>morvane.consulting@example.com</span>
      </div>
    </div>
  </div>
</body>
</html>
```